High End Home Developer

I develop 4-8 higher end spec homes in Washington DC and surrounding area. I need to build a web site so that potential purchasers can see my prior homes and know that I have done other projects.

```html
<!DOCTYPE html>
<html lang="en">
<head>
<meta charset="utf-8">
<title>Ridgeline Homes – High End Home Developer</title>
<link href="https://fonts.googleapis.com/css2?family=Montserrat:ital,wght@0,400;0,500;0,600;0,700;1,400&display=swap" rel="stylesheet">
<style>
:root{
  --gold:#d1ac3b;
  --purple:#7b1f92;
  --purple-soft:rgba(123,31,146,.88);
  --ink:#222;
  --body:#666;
  --muted:#8a8a8a;
  --light:#f4f4f4;
  --blue:#3d4cc0;
  --footer:#222327;
  --white:#fff;
}
*{box-sizing:border-box;margin:0;padding:0}
html,body{width:1200px;height:4269px;overflow:hidden}
body{font-family:"Montserrat",sans-serif;color:var(--ink);background:var(--white);position:relative}
a{color:inherit;text-decoration:none}
section,header,footer{position:absolute;left:0;width:1200px}
.eyebrow{position:absolute;font-size:18px;font-weight:500;letter-spacing:.5px;text-transform:uppercase;color:var(--ink)}
.rule{position:absolute;height:4px;background:var(--gold)}
.heading{position:absolute;font-size:40px;font-weight:700;line-height:1.2;text-transform:uppercase;color:var(--ink)}
.photo{position:absolute}

/* hero */
.hero{top:0;height:719px;background:linear-gradient(100deg,#2b2622 0%,#4a3a2e 30%,#6d655c 55%,#8b8c90 75%,#5c5f66 100%)}
.hero-shade{position:absolute;inset:0;background:linear-gradient(90deg,rgba(0,0,0,.55),rgba(0,0,0,.1) 70%)}
.brand{position:absolute;left:111px;top:34px;display:flex;align-items:center;gap:12px;color:var(--white);font-size:30px;font-weight:700;letter-spacing:2px}
.brand-mark{width:22px;height:22px;border:3px solid var(--white)}
.topbar{position:absolute;right:111px;top:28px;font-size:17px;color:var(--white);display:flex;align-items:center;gap:12px}
.topbar svg{width:16px;height:16px;fill:var(--gold)}
.nav{position:absolute;right:111px;top:71px;display:flex;gap:28px;font-size:17px;font-weight:500;color:var(--white)}
.nav .active{color:var(--gold)}
.hero-title{position:absolute;left:111px;top:272px;font-size:49px;line-height:52px;font-weight:700;color:var(--white)}
.hero-sub{position:absolute;left:111px;top:398px;font-size:22px;line-height:34px;font-weight:500;color:var(--white)}
.btn{position:absolute;display:flex;align-items:center;justify-content:center;font-size:17px;font-weight:600;text-transform:uppercase}
.btn-hero{left:111px;top:495px;width:220px;height:60px;border:2px solid var(--white);color:var(--white)}

/* story */
.story{top:719px;height:555px}
.story-video{left:111px;top:124px;width:477px;height:320px;background:linear-gradient(135deg,#d9d6d0,#f1efec 40%,#b9a89a 75%,#6c5a4f)}
.play{position:absolute;left:207px;top:128px;width:62px;height:62px;border-radius:50%;background:#222;display:flex;align-items:center;justify-content:center}
.story-text{position:absolute;left:645px;top:236px;width:455px;font-size:16px;line-height:26.5px;color:var(--body)}
.btn-outline{border:2px solid #999;color:#555;font-weight:500}

/* benefits */
.benefits{top:1274px;height:506px;background:var(--light)}
.benefit{position:absolute;top:204px;width:305px}
.benefit svg{width:96px;height:92px;stroke:var(--purple);fill:none;stroke-width:3}
.benefit h3{margin-top:26px;font-size:22px;font-weight:600;color:#333}
.benefit p{margin-top:18px;font-size:16px;line-height:26.5px;color:var(--body)}

/* properties */
.properties{top:1780px;height:760px;overflow:hidden}
.tabs{position:absolute;left:393px;top:213px;display:flex}
.tab{height:60px;padding:0 28px;display:flex;align-items:center;justify-content:center;font-size:17px;font-weight:500;background:#e8e8e8;color:#333}
.tab.active{background:var(--purple);color:var(--white)}
.card{position:absolute;top:331px;width:316px}
.card .photo{position:relative;height:283px}
.card p{margin-top:19px;font-size:21px;line-height:27px;font-weight:500;color:#333}
.arrow{position:absolute;top:467px}
.arrow svg{width:50px;height:22px;stroke:var(--white);stroke-width:5;fill:none}

/* testimonials */
.testimonials{top:2540px;height:615px;background:linear-gradient(135deg,#4a58cc,#3442b4)}
.testimonials .eyebrow{color:var(--white)}
.testimonials .rule{background:var(--white)}
.testimonials .heading{color:var(--white)}
.test-photo{left:0;top:195px;width:1200px;height:420px;background:linear-gradient(180deg,#5b6ad0 0%,#2c3a68 45%,#4d4a48 70%,#7a7775 100%)}
.quote-panel{position:absolute;left:666px;top:161px;width:534px;height:454px;background:var(--purple-soft);border-top-left-radius:100px}
.quote{position:absolute;left:70px;top:92px;width:420px;font-size:20px;line-height:31px;font-style:italic;color:var(--white)}
.author{position:absolute;left:70px;top:302px;display:flex;align-items:center;gap:16px;font-size:20px;font-weight:600;color:var(--white)}
.avatar{width:83px;height:83px;border-radius:50%;background:linear-gradient(135deg,#c9d4dc,#8a9aa6);border:3px solid var(--white)}
.q-arrows{position:absolute;left:350px;top:380px;display:flex;gap:14px}
.q-arrows svg{width:30px;height:16px;stroke:var(--white);stroke-width:3;fill:none}

/* news */
.news{top:3155px;height:711px}
.post{position:absolute;width:237px}
.post .photo{position:relative;height:172px}
.post h3{margin-top:22px;font-size:20px;font-weight:600;color:#333}
.meta{margin-top:12px;display:flex;align-items:center;gap:6px;font-size:16px;color:#555}
.meta svg{width:14px;height:14px;fill:var(--gold)}
.post p{margin-top:14px;font-size:16px;line-height:26px;color:var(--body)}
.post .more{margin-top:14px;width:22px;height:12px;stroke:#333;stroke-width:2.5;fill:none}

/* footer */
.footer{top:3866px;height:403px;background:var(--footer);color:var(--white)}
.footer-brand{position:absolute;left:111px;top:120px;display:flex;align-items:center;gap:18px;font-size:50px;font-weight:700;letter-spacing:3px}
.footer-brand .brand-mark{width:40px;height:40px;border-width:5px}
.col-title{position:absolute;top:74px;font-size:19px;font-weight:600}
.links{position:absolute;left:519px;top:107px;list-style:none;font-size:17px;line-height:33px}
.contact{position:absolute;left:708px;top:107px;font-size:17px;line-height:27px}
.contact li{list-style:none;display:flex;gap:14px;margin-bottom:25px}
.contact svg{width:15px;height:17px;fill:var(--gold);flex:none;margin-top:5px}
.footer-rule{position:absolute;left:111px;top:305px;width:978px;height:1px;background:#555}
.copyright{position:absolute;left:111px;top:341px;font-size:17px}
.social{position:absolute;left:941px;top:330px;display:flex;gap:12px}
.social span{width:40px;height:40px;border-radius:50%;border:2px solid var(--gold)}
</style>
</head>
<body>

<header class="hero">
  <div class="photo" style="inset:0;background:inherit" role="img" aria-label="Photograph of a modern two-storey home with white board-and-batten siding and a stone terrace at dusk among autumn trees"></div>
  <div class="hero-shade"></div>
  <div class="brand"><span class="brand-mark"></span>RIDGELINE</div>
  <div class="topbar">
    <svg viewBox="0 0 24 24"><path d="M6.6 10.8a15.5 15.5 0 0 0 6.6 6.6l2.2-2.2c.3-.3.7-.4 1-.2 1.1.4 2.3.6 3.6.6.6 0 1 .4 1 1V20c0 .6-.4 1-1 1A17 17 0 0 1 3 4c0-.6.4-1 1-1h3.5c.6 0 1 .4 1 1 0 1.3.2 2.5.6 3.6.1.3 0 .7-.2 1z"/></svg>
    <span>1 555 010 0188</span><span>|</span>
    <svg viewBox="0 0 24 24"><path d="M2 5h20v14H2z M2 5l10 8 10-8" /></svg>
    <span>info@ridgelinehomes.com</span>
  </div>
  <nav class="nav">
    <a class="active">HOME</a><a>ABOUT</a><a>PROPERTIES</a><a>NEWS</a><a>CONTACT</a>
  </nav>
  <div class="rule" style="left:0;top:230px;width:345px"></div>
  <h1 class="hero-title">HIGH END<br>HOME DEVELOPER</h1>
  <p class="hero-sub">I develop 4-8 higher end spec homes<br>in Washington DC and surrounding area.</p>
  <a class="btn btn-hero">Explore Projects</a>
</header>

<section class="story">
  <div class="photo story-video" role="img" aria-label="Photograph of hands holding architectural floor plans over a desk">
    <span class="play"><svg width="20" height="22" viewBox="0 0 20 22"><path d="M3 2l15 9-15 9z" fill="#fff"/></svg></span>
  </div>
  <span class="eyebrow" style="left:645px;top:64px">Our Story</span>
  <div class="rule" style="left:807px;top:74px;width:393px"></div>
  <h2 class="heading" style="left:645px;top:116px">Welcome to<br>Ridgeline Homes</h2>
  <p class="story-text">Lorem ipsum dolor sit amet, consectetur adipiscing elit, sed do eiusmod tempor incididunt ut labore et dolorlie magna aliqua. Ut enim ad minim veniam, quis nostrud exercitation ullamco laboris nisi ut aliquip ex ea comm odo consequat. Duis aute irure dolor in reprehenderit in voluptate velit esse cillum dolore.</p>
  <a class="btn btn-outline" style="left:645px;top:416px;width:162px;height:58px">Read More</a>
</section>

<section class="benefits">
  <div class="rule" style="left:0;top:63px;width:348px"></div>
  <span class="eyebrow" style="left:370px;top:52px">Benefits</span>
  <h2 class="heading" style="left:111px;top:100px">Why Choose Us</h2>

  <div class="benefit" style="left:111px">
    <svg viewBox="0 0 96 92"><rect x="3" y="22" width="86" height="66"/><path d="M3 50h30v38M33 50V22M55 22v30h34M55 64h20v24M70 4l22 22-20 20"/></svg>
    <h3>Customizable home plans</h3>
    <p>Duis aute irure dolor in reprehenderit in voluptate velit esse cillum dolore eu fugiat nulla pariatur.</p>
  </div>
  <div class="benefit" style="left:449px">
    <svg viewBox="0 0 96 92"><path d="M20 40L48 14l28 26M28 34v26h40V34M42 60V46h12v14M6 50l14 30h14M90 50L76 80H62"/></svg>
    <h3>High End Home Developer</h3>
    <p>Duis aute irure dolor in reprehenderit in voluptate velit esse cillum dolore eu fugiat nulla pariatur.</p>
  </div>
  <div class="benefit" style="left:789px">
    <svg viewBox="0 0 96 92"><rect x="3" y="10" width="80" height="66" rx="4"/><path d="M3 26h80M20 3v14M42 3v14M64 3v14"/><circle cx="74" cy="70" r="18" fill="#f4f4f4"/><path d="M74 60v10l7 5"/><path d="M16 40h4M30 40h4M44 40h4M58 40h4M16 54h4M30 54h4M44 54h4"/></svg>
    <h3>Build Time</h3>
    <p>Duis aute irure dolor in reprehenderit in voluptate velit esse cillum dolore eu fugiat nulla pariatur.</p>
  </div>
</section>

<section class="properties">
  <span class="eyebrow" style="left:896px;top:78px">Gallery</span>
  <div class="rule" style="left:1047px;top:88px;width:153px"></div>
  <h2 class="heading" style="left:651px;top:120px">Our Properties</h2>
  <div class="tabs">
    <span class="tab active">RIDGELINE PROPERTIES</span>
    <span class="tab">ALDER PROPERTIES</span>
  </div>

  <div class="card" style="left:111px">
    <div class="photo" style="background:linear-gradient(180deg,#9fb3c9,#e9e5dc 40%,#7d6a55 100%)" role="img" aria-label="Photograph of a renovated white rowhouse with a front porch"></div>
    <p>140 Elm Row NE, WDC<br>20090</p>
  </div>
  <div class="card" style="left:442px">
    <div class="photo" style="background:linear-gradient(180deg,#3d4a2c,#6f6d63 45%,#2f2f32 100%)" role="img" aria-label="Photograph of a modern three-storey home with balconies and double garage"></div>
    <p>5820 Birchwood Ln NW,<br>WDC 2009</p>
  </div>
  <div class="card" style="left:772px">
    <div class="photo" style="background:linear-gradient(180deg,#5d93d6,#c48a4c 45%,#8d7a5e 70%,#5f7e3b 100%)" role="img" aria-label="Photograph of a stone house with autumn trees and lawn"></div>
    <p>3475 Larkspur St NW,<br>WDC</p>
  </div>
  <div class="card" style="left:1102px">
    <div class="photo" style="background:linear-gradient(180deg,#6fa0dc,#b7a99a 55%,#6b8f45 100%)" role="img" aria-label="Photograph of a single-storey brick home with lawn"></div>
    <p>3388 Oakmere Ct,<br>WDC 20098</p>
  </div>
  <span class="arrow" style="left:82px"><svg viewBox="0 0 50 22"><path d="M48 11H4M14 2L4 11l10 9"/></svg></span>
  <span class="arrow" style="left:1070px"><svg viewBox="0 0 50 22"><path d="M2 11h44M36 2l10 9-10 9"/></svg></span>
</section>

<section class="testimonials">
  <div class="photo test-photo" role="img" aria-label="Photograph of a large modern home with lit garage doors at dusk"></div>
  <div class="rule" style="left:0;top:82px;width:295px"></div>
  <span class="eyebrow" style="left:320px;top:72px;color:var(--white)">Reviews</span>
  <h2 class="heading" style="left:111px;top:120px">Testimonials</h2>
  <div class="quote-panel">
    <p class="quote">“ Lorem ipsum dolor sit amet, constr adipiscing elit, sed do eiusmod tem por incididunt ut labore et dolore ma gna aliqua. Ut enim ad minim vequis nostrud exercitation ullamco laboris nisi ut aliquip ex ea.”</p>
    <div class="author"><span class="avatar" role="img" aria-label="Customer portrait"></span>John Doe</div>
    <div class="q-arrows">
      <svg viewBox="0 0 30 16"><path d="M29 8H3M10 2L3 8l7 6"/></svg>
      <svg viewBox="0 0 30 16"><path d="M1 8h26M20 2l7 6-7 6"/></svg>
    </div>
  </div>
</section>

<section class="news">
  <span class="eyebrow" style="left:802px;top:74px">Post</span>
  <div class="rule" style="left:880px;top:84px;width:320px"></div>
  <h2 class="heading" style="left:802px;top:118px">Latest News</h2>

  <article class="post" style="left:111px;top:151px">
    <div class="photo" style="background:linear-gradient(180deg,#2f4f8c,#e8c98f 60%,#2aa4d8)" role="img" aria-label="Photograph of a modern villa with a pool at night"></div>
    <h3>Duis aute irure dolor</h3>
    <div class="meta"><svg viewBox="0 0 14 14"><rect x="1" y="2" width="12" height="11"/></svg>22/11/22 &nbsp;| <svg viewBox="0 0 14 14"><circle cx="7" cy="4" r="3"/><path d="M1 14a6 6 0 0 1 12 0z"/></svg>Admin</div>
    <p>Lorem ipsum dolor sit amet, consectetur adipiscing elit, sed do eiusmod..</p>
    <svg class="more" viewBox="0 0 22 12"><path d="M1 6h19M15 1l5 5-5 5"/></svg>
  </article>
  <article class="post" style="left:358px;top:186px">
    <div class="photo" style="background:linear-gradient(180deg,#7c8288,#c9c6c1 50%,#6b4a36)" role="img" aria-label="Photograph of a wooden deck with outdoor sofa"></div>
    <h3>Duis aute irure dolor</h3>
    <div class="meta"><svg viewBox="0 0 14 14"><rect x="1" y="2" width="12" height="11"/></svg>22/11/22 &nbsp;| <svg viewBox="0 0 14 14"><circle cx="7" cy="4" r="3"/><path d="M1 14a6 6 0 0 1 12 0z"/></svg>Admin</div>
    <p>Lorem ipsum dolor sit amet, consectetur adipiscing elit, sed do eiusmod..</p>
    <svg class="more" viewBox="0 0 22 12"><path d="M1 6h19M15 1l5 5-5 5"/></svg>
  </article>
  <article class="post" style="left:605px;top:229px">
    <div class="photo" style="background:linear-gradient(180deg,#f2f2f0,#c7b7a3 50%,#2fb3c4)" role="img" aria-label="Photograph of a white modern house with pool"></div>
    <h3>Duis aute irure dolor</h3>
    <div class="meta"><svg viewBox="0 0 14 14"><rect x="1" y="2" width="12" height="11"/></svg>22/11/22 &nbsp;| <svg viewBox="0 0 14 14"><circle cx="7" cy="4" r="3"/><path d="M1 14a6 6 0 0 1 12 0z"/></svg>Admin</div>
    <p>Lorem ipsum dolor sit amet, consectetur adipiscing elit, sed do eiusmod..</p>
    <svg class="more" viewBox="0 0 22 12"><path d="M1 6h19M15 1l5 5-5 5"/></svg>
  </article>
  <article class="post" style="left:852px;top:272px">
    <div class="photo" style="background:linear-gradient(180deg,#f4f6f8,#48586a 45%,#4f9a33)" role="img" aria-label="Photograph of a large family home with green lawn"></div>
    <h3>Duis aute irure dolor</h3>
    <div class="meta"><svg viewBox="0 0 14 14"><rect x="1" y="2" width="12" height="11"/></svg>22/11/22 &nbsp;| <svg viewBox="0 0 14 14"><circle cx="7" cy="4" r="3"/><path d="M1 14a6 6 0 0 1 12 0z"/></svg>Admin</div>
    <p>Lorem ipsum dolor sit amet, consectetur adipiscing elit, sed do eiusmod..</p>
    <svg class="more" viewBox="0 0 22 12"><path d="M1 6h19M15 1l5 5-5 5"/></svg>
  </article>
</section>

<footer class="footer">
  <div class="footer-brand"><span class="brand-mark"></span>RIDGELINE</div>
  <span class="col-title" style="left:519px">Quick Links</span>
  <ul class="links"><li>Home</li><li>About</li><li>Properties</li><li>News</li><li>Contact</li></ul>
  <span class="col-title" style="left:708px">Contact Information</span>
  <ul class="contact">
    <li><svg viewBox="0 0 14 17"><path d="M7 0a6 6 0 0 0-6 6c0 5 6 11 6 11s6-6 6-11a6 6 0 0 0-6-6zm0 8a2 2 0 1 1 0-4 2 2 0 0 1 0 4z"/></svg><span>No 123 uis aute irlor in reprehen<br>derit in voluptate velit</span></li>
    <li><svg viewBox="0 0 24 24"><path d="M6.6 10.8a15.5 15.5 0 0 0 6.6 6.6l2.2-2.2c.3-.3.7-.4 1-.2 1.1.4 2.3.6 3.6.6.6 0 1 .4 1 1V20c0 .6-.4 1-1 1A17 17 0 0 1 3 4c0-.6.4-1 1-1h3.5c.6 0 1 .4 1 1 0 1.3.2 2.5.6 3.6.1.3 0 .7-.2 1z"/></svg><span>1 555 010 0188</span></li>
    <li><svg viewBox="0 0 24 20"><path d="M1 2h22v16H1z"/></svg><span>info@ridgelinehomes.com</span></li>
  </ul>
  <div class="footer-rule"></div>
  <p class="copyright">Copyright © 2022 Ridgeline Homes - all rights reserved.</p>
  <div class="social"><span></span><span></span><span></span></div>
</footer>

</body>
</html>
```